Cookie Box Packaging

We are looking for a Box for our Shortbread Cookies. They are traditional shortbread middle to high end of the market. Made with butter. We already have a successful product and would like to use the brand but not necessarily the style.

We like our design to be an mix of vintage and modern - we are open to all colours. The competition on the supermarket shelf is stiff and we need to stand out in grocery not in the gourmet food market. Our thinking is simple rather than the craziness and chaos that comes with a supermarket shelf.
Attached are some Box Ideas, created in-house, along with a black shortbread box idea , which we loved but didn't really fit into the grocery section of the supermarket. Make us stand out in the grocery shelf! I have also uploaded a logo. Our brand is not necessary but, is there if you wanted to use it. I have also uploaded our other product/packet design so you can see the brand of our other cookie which is positioned in bakery /deli not grocery.

I look forward to seeing the results

```html
<!DOCTYPE html>
<html lang="en">
<head>
<meta charset="utf-8">
<title>Bramble Cookies – Butter Shortbread Box</title>
<link href="https://fonts.googleapis.com/css2?family=Montserrat:wght@400;700;800&display=swap" rel="stylesheet">
<style>
  :root {
    --backdrop: #f4f4f4;
    --gingham-pink: #f3cdd3;
    --band-black: #0c0c0c;
    --ink: #111111;
    --muted-ink: #555555;
    --paper-white: #ffffff;
    --soft-white: #cfcfcf;
    --crumb-light: #f2e6cf;
    --crumb-dark: #d6c39c;
  }
  * { margin: 0; padding: 0; box-sizing: border-box; }
  html, body {
    width: 1200px; height: 675px; overflow: hidden;
    background: var(--backdrop);
    font-family: "Montserrat", sans-serif;
  }
  .canvas { position: relative; width: 1200px; height: 675px; }

  /* Box dieline: front + right side panel, laid flat */
  .dieline {
    position: absolute; left: 315px; top: 42px;
    display: flex; height: 590px;
    box-shadow: 0 2px 10px rgba(0,0,0,0.08);
  }
  .box-front {
    position: relative; width: 340px; height: 590px;
    background: var(--gingham-pink); overflow: hidden;
  }
  .box-side {
    position: relative; width: 230px; height: 590px;
    background: var(--band-black); overflow: hidden;
    border-left: 1px solid #2a2a2a;
  }

  .black-band { position: absolute; inset: 0; width: 100%; height: 100%; }

  .brand-name {
    position: absolute; left: 0; right: 0; top: 160px;
    text-align: center; color: var(--paper-white);
    font-weight: 800; font-size: 46px; letter-spacing: -1px; line-height: 1;
  }
  .brand-name .brand-sub {
    display: block; font-size: 24px; letter-spacing: 0;
    margin-top: 2px; padding-left: 130px;
  }

  .product-title {
    position: absolute; left: 18px; top: 266px;
    color: var(--paper-white);
    font-weight: 800; font-size: 31px; letter-spacing: -0.5px; line-height: 1;
  }
  .product-title .title-tag {
    position: absolute; right: 0; top: -9px;
    font-size: 7.5px; font-weight: 800; letter-spacing: 0.3px;
  }
  .ingredients {
    position: absolute; left: 18px; top: 302px; width: 232px;
    color: var(--paper-white);
    font-size: 6.8px; font-weight: 800; line-height: 1.2;
  }
  .product-blurb {
    position: absolute; left: 18px; top: 313px; width: 222px;
    color: var(--paper-white);
    font-size: 5.9px; line-height: 1.3; text-align: justify;
  }
  .cookie-stack {
    position: absolute; left: 252px; top: 276px;
    width: 78px; height: 190px;
    border-radius: 34px 34px 14px 14px;
    background: linear-gradient(180deg, var(--crumb-light) 0%, var(--crumb-dark) 100%);
  }
  .origin-badge { position: absolute; left: 26px; top: 392px; width: 86px; height: 86px; }

  .net-weight {
    position: absolute; left: 48px; top: 516px;
    font-weight: 700; font-size: 15px; color: var(--ink);
  }
  .info-divider {
    position: absolute; left: 112px; top: 506px;
    width: 1.5px; height: 40px; background: var(--ink);
  }
  .info-note {
    position: absolute; left: 124px; top: 510px; width: 200px;
    font-size: 6.2px; line-height: 1.35; color: var(--muted-ink); text-align: justify;
  }
  .info-note strong { display: block; color: var(--ink); font-weight: 700; }

  /* Side panel */
  .side-brand {
    position: absolute; left: 0; right: 0; top: 96px;
    text-align: center; color: var(--paper-white);
    font-weight: 800; font-size: 32px; letter-spacing: -0.5px; line-height: 1;
  }
  .side-brand .brand-sub { display: block; font-size: 17px; margin-top: 2px; padding-left: 80px; }
  .about-title {
    position: absolute; left: 24px; top: 300px;
    color: var(--paper-white); font-weight: 800; font-size: 15px;
  }
  .about-copy {
    position: absolute; left: 24px; top: 324px; width: 180px;
    color: var(--soft-white); font-size: 6.4px; line-height: 1.4; text-align: justify;
  }
</style>
</head>
<body>
<main class="canvas">
  <div class="dieline">
    <section class="box-front">
      <svg class="black-band" viewBox="0 0 340 590" preserveAspectRatio="none" aria-hidden="true">
        <path d="M0 150 C 100 138, 210 128, 340 112 L340 400 C 250 380, 130 340, 0 372 Z" fill="var(--band-black)"/>
      </svg>

      <h1 class="brand-name">Bramble<span class="brand-sub">cookies</span></h1>

      <h2 class="product-title">Shortbread<span class="title-tag">BUTTER</span></h2>
      <p class="ingredients">Ingredients Butter Flour Sugar Cornstarch Cream</p>
      <p class="product-blurb">Lorem ipsum dolor sit amet, consectetur adipiscing elit. Donec turpis mauris, dapibus vel dictum et, faucibus feugiat elit. Class aptent taciti sociosqu ad litora torquent per conubia nostra, per inceptos himenaeos. Mauris tincidunt a ex at sagittis.</p>

      <div class="cookie-stack" role="img" aria-label="Photo of a stack of round butter shortbread cookies, the top one bitten"></div>

      <svg class="origin-badge" viewBox="0 0 100 100" role="img" aria-label="Origin badge">
        <circle cx="50" cy="50" r="46" fill="none" stroke="var(--ink)" stroke-width="2"/>
      </svg>

      <span class="net-weight">250 g</span>
      <span class="info-divider"></span>
      <p class="info-note"><strong>Lorem ipsum dolor</strong>sit amet, consectetur adipiscing elit. Donec turpis mauris, dapibus vel dictum et, faucibus feugiat elit.</p>
    </section>

    <section class="box-side">
      <p class="side-brand">Bramble<span class="brand-sub">cookies</span></p>
      <h3 class="about-title">About Us</h3>
      <p class="about-copy">Baked in small batches with real butter, our shortbread keeps a simple recipe that has been shared around the family table for generations.</p>
    </section>
  </div>
</main>
</body>
</html>
```